Etiketten für Dips
Zielgruppe
Landwirtschaft mit Direktvermarktung und Diversifikation durch workshops und Beratung zur Selbstversorgung
Zielgruppe: LOHAS, Best Agers
Aufgabenstellung
es gibt pikante und süße Dips (Weiters Salz und Essig) unter dem Motto 'Würzen | Dippen | Toppen' (das soll unbedingt überall mit drauf aufs Etikett), Etikett passend zum Logo - möglicherweise Teile davon auch am Etikett? durchscheinend aber farbig? die Etiketten jeweils in unterschiedlichen 'Farbmotto' so dass eine bunte aber gediegene Serie mit Wiedererkennung entstehen die höheres Preissegment gerecht wird/unterstreicht. Etikett soll nur 1 Teil sein, da am Deckel der Gläser ohnehin das Logoetikett drauf kommt. Bei Siegerprojekt gerne weitere Zusammenarbeit für die weiteren Etiketten.
Produkte für die Etiketten benötigt werden: Mara Bunt (Tomaten-Dip), Brisa Paul (Salz mit Tomaten), Sommer-Rübli (Grillsauce/-dip), Moosgeflüster (Lebkuchenmarmelade), Wild Mango, Kornbrise (Gewürzessig mit Chilli)
Bitte an alle notwendigen Inhalte eines Lebensmitteletiketts denken bzw Platzhalter einfügen

```html
<!DOCTYPE html>
<html lang="de">
<head>
<meta charset="utf-8">
<title>Beetglück – Etiketten</title>
<link rel="stylesheet" href="https://fonts.googleapis.com/css2?family=Anton&family=Montserrat:wght@800;900&family=Source+Sans+3:wght@400;700&display=swap">
<style>
:root{
  --band-green:#22301f;
  --band-red:#8b1915;
  --band-navy:#1a2640;
  --cream:#f6f3e9;
  --ink:#1b1b1b;
  --white:#ffffff;
}
*{box-sizing:border-box;margin:0;padding:0}
html,body{width:901px;height:1200px;overflow:hidden}
body{position:relative;font-family:"Source Sans 3",Arial,sans-serif;color:var(--ink)}
.band{position:absolute;left:0;width:901px;height:400px}
.band--green{top:0;background:var(--band-green)}
.band--red{top:400px;background:var(--band-red)}
.band--navy{top:800px;background:var(--band-navy)}

.label{position:absolute;left:92px;top:174px;width:697px;height:125px;display:flex}
.label-info,.label-facts{background:var(--cream);position:relative}
.label-info{width:213px}
.label-front{width:270px;position:relative;overflow:hidden;color:var(--white)}
.label-facts{width:214px}

.info-title{position:absolute;left:58px;top:17px;font-weight:700;font-size:11.5px;letter-spacing:-.1px}
.info-text{position:absolute;left:25px;top:33px;width:169px;font-size:6.3px;line-height:8.1px;text-align:justify}
.info-motto{position:absolute;left:25px;top:103px;font-size:6.3px;font-weight:700}
.info-url{position:absolute;right:19px;top:103px;font-size:6.3px;font-weight:700}

.front-art{position:absolute;inset:0;width:100%;height:100%}
.front-title{position:absolute;font-family:"Montserrat",Arial,sans-serif;font-weight:900;line-height:.96;text-transform:uppercase}
.front-volume,.front-kind{position:absolute;font-family:"Montserrat",Arial,sans-serif;font-weight:800;font-size:11px;line-height:1}
.front-volume{left:50px;top:106px}
.front-kind{top:106px}

.facts-rule{position:absolute;background:var(--ink)}
.facts-rule--top{left:9px;top:8px;width:187px;height:.6px}
.facts-rule--mid{left:9px;top:90px;width:187px;height:.6px}
.facts-rule--bottom{left:9px;top:117px;width:187px;height:.6px}
.facts-rule--col{left:98px;top:8px;width:.6px;height:109px}
.facts-rule--logo{left:52px;top:90px;width:.6px;height:27px}
.best-before-box{position:absolute;left:10px;top:15px;width:16px;height:66px;background:var(--white)}
.best-before{position:absolute;left:29px;top:15px;writing-mode:vertical-rl;font-size:7.5px}
.facts-name{position:absolute;left:56px;top:13px;font-family:"Anton",Impact,sans-serif;font-size:27px;line-height:23px;text-transform:uppercase;letter-spacing:-.5px}
.facts-motto{position:absolute;left:102px;top:14px;font-family:"Montserrat",Arial,sans-serif;font-weight:800;font-size:10.5px;line-height:9.2px}
.facts-ingredients{position:absolute;left:102px;top:52px;width:108px;font-size:8px;line-height:11px}
.facts-ingredients b{font-weight:700}
.facts-brand{position:absolute;left:56px;top:97px;font-size:10px;line-height:1}
.facts-address{position:absolute;left:102px;top:93px;font-size:7.8px;line-height:11px}
</style>
</head>
<body>

<section class="band band--green">
  <article class="label">
    <div class="label-info">
      <h2 class="info-title">Was ist Beetglück?</h2>
      <p class="info-text">Erde zwischen den Fingern, der Duft von frischen Kräutern und das Glück, die erste selbst geerntete Tomate auf der Zunge zergehen zu lassen – genau das ist Gartenfreude! Bei Beetglück dreht sich alles um nachhaltige Gartengestaltung, kreative Selbstversorgung und puren Genuss direkt aus der Natur. Entdecke, wie du mit meinen Workshops, Vorträgen und Produkten deine eigene grüne Oase erschaffst – ganz ohne Chemie, dafür mit viel Herz und frischen Ideen.</p>
      <p class="info-motto">Würzen | Dippen | Toppen</p>
      <p class="info-url">www.beetglueck-beispiel.at</p>
    </div>
    <div class="label-front">
      <svg class="front-art" role="img" aria-label="Gemüse-Illustration in Grüntönen" viewBox="0 0 270 125" preserveAspectRatio="none">
        <defs><linearGradient id="g-green" x1="0" y1="0" x2="1" y2="1"><stop offset="0" stop-color="#7aa354"/><stop offset="1" stop-color="#86b061"/></linearGradient></defs>
        <rect width="270" height="125" fill="url(#g-green)"/>
      </svg>
      <h1 class="front-title" style="left:107px;top:20px;font-size:24px;line-height:25.5px">Som<br>mer<br>Rüb<br>li</h1>
      <span class="front-volume">370 ml</span>
      <span class="front-kind" style="left:175px">Grillsauce</span>
    </div>
    <div class="label-facts">
      <span class="facts-rule facts-rule--top"></span><span class="facts-rule facts-rule--mid"></span><span class="facts-rule facts-rule--bottom"></span><span class="facts-rule facts-rule--col"></span><span class="facts-rule facts-rule--logo"></span>
      <span class="best-before-box"></span><span class="best-before">haltbar bis:</span>
      <p class="facts-name" style="top:20px;font-size:29px;line-height:27px">Rüb<br>li</p>
      <p class="facts-motto">Wos ma gern<br>mocht, mocht<br>ma guad!</p>
      <p class="facts-ingredients"><b>Zutaten:</b> Karotten, Chilli, Salz, Zucker, frische Kräuter</p>
      <p class="facts-brand">Beetglück</p>
      <p class="facts-address">Lena Haidacher<br>Wiesenweg 7, 3100 Ackerfeld</p>
    </div>
  </article>
</section>

<section class="band band--red">
  <article class="label" style="top:173px">
    <div class="label-info">
      <h2 class="info-title">Was ist Beetglück?</h2>
      <p class="info-text">Erde zwischen den Fingern, der Duft von frischen Kräutern und das Glück, die erste selbst geerntete Tomate auf der Zunge zergehen zu lassen – genau das ist Gartenfreude! Bei Beetglück dreht sich alles um nachhaltige Gartengestaltung, kreative Selbstversorgung und puren Genuss direkt aus der Natur. Entdecke, wie du mit meinen Workshops, Vorträgen und Produkten deine eigene grüne Oase erschaffst – ganz ohne Chemie, dafür mit viel Herz und frischen Ideen.</p>
      <p class="info-motto">Würzen | Dippen | Toppen</p>
      <p class="info-url">www.beetglueck-beispiel.at</p>
    </div>
    <div class="label-front">
      <svg class="front-art" role="img" aria-label="Tomaten-Illustration in Rot- und Orangetönen" viewBox="0 0 270 125" preserveAspectRatio="none">
        <defs><linearGradient id="g-red" x1="0" y1="0" x2="1" y2="1"><stop offset="0" stop-color="#e2262a"/><stop offset=".5" stop-color="#e43a2e"/><stop offset="1" stop-color="#e2262a"/></linearGradient></defs>
        <rect width="270" height="125" fill="url(#g-red)"/>
      </svg>
      <h1 class="front-title" style="left:104px;top:50px;font-size:24px;line-height:25px">Mara<br>Bunt</h1>
      <span class="front-volume">370 ml</span>
      <span class="front-kind" style="left:169px">Tomatendip</span>
    </div>
    <div class="label-facts">
      <span class="facts-rule facts-rule--top"></span><span class="facts-rule facts-rule--mid"></span><span class="facts-rule facts-rule--bottom"></span><span class="facts-rule facts-rule--col"></span><span class="facts-rule facts-rule--logo"></span>
      <span class="best-before-box"></span><span class="best-before">haltbar bis:</span>
      <p class="facts-name" style="font-size:23px;line-height:23px;letter-spacing:-.8px">Ma<br>ra<br>Bunt</p>
      <p class="facts-motto">Wos ma gern<br>mocht, mocht<br>ma guad!</p>
      <p class="facts-ingredients"><b>Zutaten:</b> Tomaten, Chilli, Salz, Zucker, frische Kräuter</p>
      <p class="facts-brand">Beetglück</p>
      <p class="facts-address">Lena Haidacher<br>Wiesenweg 7, 3100 Ackerfeld</p>
    </div>
  </article>
</section>

<section class="band band--navy">
  <article class="label">
    <div class="label-info">
      <h2 class="info-title">Was ist Beetglück?</h2>
      <p class="info-text">Erde zwischen den Fingern, der Duft von frischen Kräutern und das Glück, die erste selbst geerntete Tomate auf der Zunge zergehen zu lassen – genau das ist Gartenfreude! Bei Beetglück dreht sich alles um nachhaltige Gartengestaltung, kreative Selbstversorgung und puren Genuss direkt aus der Natur. Entdecke, wie du mit meinen Workshops, Vorträgen und Produkten deine eigene grüne Oase erschaffst – ganz ohne Chemie, dafür mit viel Herz und frischen Ideen.</p>
      <p class="info-motto">Würzen | Dippen | Toppen</p>
      <p class="info-url">www.beetglueck-beispiel.at</p>
    </div>
    <div class="label-front">
      <svg class="front-art" role="img" aria-label="Zwetschken-Illustration in Beeren- und Blautönen" viewBox="0 0 270 125" preserveAspectRatio="none">
        <defs><linearGradient id="g-plum" x1="0" y1="0" x2="1" y2="1"><stop offset="0" stop-color="#b02c5f"/><stop offset=".55" stop-color="#8e3164"/><stop offset="1" stop-color="#b02c5f"/></linearGradient></defs>
        <rect width="270" height="125" fill="url(#g-plum)"/>
      </svg>
      <h1 class="front-title" style="left:101px;top:20px;font-size:23px;line-height:25.5px">Moos<br>ge<br>flüs<br>ter</h1>
      <span class="front-volume">370 ml</span>
      <span class="front-kind" style="left:167px;top:100px;font-size:10.5px;line-height:10px">Lebkuchen-<br>marmelade</span>
    </div>
    <div class="label-facts">
      <span class="facts-rule facts-rule--top"></span><span class="facts-rule facts-rule--mid"></span><span class="facts-rule facts-rule--bottom"></span><span class="facts-rule facts-rule--col"></span><span class="facts-rule facts-rule--logo"></span>
      <span class="best-before-box"></span><span class="best-before">haltbar bis:</span>
      <p class="facts-name" style="left:45px">Zwe<br>tsch<br>ke</p>
      <p class="facts-motto">Wos ma gern<br>mocht, mocht<br>ma guad!</p>
      <p class="facts-ingredients"><b>Zutaten:</b> Zwetschke, Zucker, Zimt, Nelke</p>
      <p class="facts-brand">Beetglück</p>
      <p class="facts-address">Lena Haidacher<br>Wiesenweg 7, 3100 Ackerfeld</p>
    </div>
  </article>
</section>

</body>
</html>
```